Tessavale Communications

I need a very clean, uncomplicated design for an LA-based, very senior level strategic communications firm with about four associates. Landing page should stress LA, maybe a slider with downtown skyline, Malibu pier, and Rodeo Drive. In addition to landing page with firm's description, all else we'd need is services offered page and another for bios of associates.

Industry/Entity Type

Communications

Font styles to use
Sans Serif

```html
<!DOCTYPE html>
<html lang="en">
<head>
<meta charset="utf-8">
<title>Tessavale Communications</title>
<link rel="stylesheet" href="https://fonts.googleapis.com/css2?family=Raleway:wght@300;400;500&family=Open+Sans:wght@300;400&display=swap">
<style>
  :root {
    --brand-blue: #2172b0;
    --ink: #444444;
    --ink-soft: #666666;
    --nav-grey: #888888;
    --page-bg: #f7f7f7;
    --white: #ffffff;
    --rule: #dddddd;
    --footer-bg: #202020;
    --footer-text: #8a8a8a;
  }
  * { margin: 0; padding: 0; box-sizing: border-box; }
  html, body { width: 1021px; height: 1200px; overflow: hidden; }
  body {
    background: var(--page-bg);
    font-family: "Raleway", sans-serif;
    color: var(--ink);
    position: relative;
  }

  .site-header {
    height: 86px;
    background: var(--white);
    position: relative;
  }
  .brand {
    position: absolute; left: 76px; top: 41px;
    display: flex; align-items: center; gap: 5px;
    font-size: 10.5px; font-weight: 500; color: var(--brand-blue);
  }
  .brand-dot {
    width: 15px; height: 15px; border-radius: 50%;
    border: 2.5px solid var(--brand-blue);
  }
  .main-nav {
    position: absolute; right: 105px; top: 43px;
    display: flex; gap: 16px;
    font-size: 10px; color: var(--nav-grey);
  }
  .main-nav .is-current { color: var(--brand-blue); }
  .nav-divider {
    position: absolute; left: 911px; top: 42px;
    width: 1px; height: 18px; background: var(--rule);
  }
  .search-icon { position: absolute; left: 930px; top: 44px; }

  .hero {
    height: 478px; position: relative; overflow: hidden;
  }
  .hero-photo {
    position: absolute; inset: 0;
    background: linear-gradient(180deg, #8d8a80 0%, #b3a68e 22%, #6f6a62 48%, #4b4d4c 72%, #3d3f40 100%);
  }
  .hero-title {
    position: absolute; left: 65px; top: 272px;
    font-size: 36px; font-weight: 300; color: var(--white);
    letter-spacing: -0.3px;
  }
  .hero-actions {
    position: absolute; left: 65px; top: 246px;
    display: flex; gap: 13px; margin-top: 86px;
  }
  .btn {
    height: 38px; display: flex; align-items: center; justify-content: center;
    font-size: 10px; letter-spacing: 1.6px; color: var(--white);
  }
  .btn-primary { width: 115px; background: var(--brand-blue); }
  .btn-outline { width: 63px; border: 1.5px solid var(--white); }
  .slider-arrow {
    position: absolute; top: 224px; width: 40px; height: 48px;
    background: rgba(0,0,0,0.18);
    display: flex; align-items: center; justify-content: center;
  }
  .slider-arrow.prev { left: 0; }
  .slider-arrow.next { right: 0; }
  .slider-dots {
    position: absolute; top: 532px; left: 0; right: 0; margin-top: -86px;
    display: flex; justify-content: center; gap: 7px;
  }
  .slider-dots span {
    width: 8px; height: 8px; border-radius: 50%;
    border: 1px solid var(--white);
  }
  .slider-dots .is-active { background: var(--white); }

  .intro { padding: 0 73px; }
  .intro-heading {
    text-align: center; font-weight: 400; font-size: 22.5px;
    color: var(--ink); padding-top: 56px; letter-spacing: -0.3px;
  }
  .intro-rule { height: 1px; background: var(--rule); margin-top: 30px; }
  .intro-columns {
    display: flex; gap: 21px; margin-top: 67px;
  }
  .intro-columns p {
    flex: 1; font-size: 13px; font-weight: 300; line-height: 27.4px;
    text-align: justify; color: var(--ink);
  }

  .testimonial { text-align: center; margin-top: 22px; font-family: "Open Sans", sans-serif; }
  .testimonial-quote { font-size: 18px; font-weight: 400; color: #333; }
  .testimonial-author { font-size: 13px; color: var(--ink-soft); margin-top: 25px; }
  .testimonial-dots { display: flex; justify-content: center; gap: 7px; margin-top: 28px; }
  .testimonial-dots span {
    width: 8px; height: 8px; border-radius: 50%; border: 1px solid #333;
  }
  .testimonial-dots .is-active { background: #333; }

  .site-footer {
    position: absolute; left: 0; right: 0; top: 1131px; bottom: 0;
    background: var(--footer-bg);
  }
  .copyright {
    position: absolute; left: 73px; top: 27px;
    font-size: 9.5px; font-weight: 300; color: var(--footer-text);
  }
  .social { position: absolute; right: 75px; top: 26px; display: flex; gap: 14px; }
  .social span { width: 12px; height: 12px; border-radius: 50%; background: var(--footer-text); }
</style>
</head>
<body>
  <header class="site-header">
    <div class="brand"><span class="brand-dot"></span>Tessavale Communications</div>
    <nav class="main-nav">
      <span class="is-current">Home</span>
      <span>Services Offered</span>
      <span>Associates</span>
      <span>Contact</span>
    </nav>
    <span class="nav-divider"></span>
    <svg class="search-icon" width="13" height="13" viewBox="0 0 13 13" fill="none" stroke="#999" stroke-width="1.4">
      <circle cx="5.3" cy="5.3" r="4.3"/><line x1="8.5" y1="8.5" x2="12.3" y2="12.3"/>
    </svg>
  </header>

  <section class="hero">
    <div class="hero-photo" role="img" aria-label="Downtown Los Angeles skyline at sunset above a busy multi-lane boulevard"></div>
    <h1 class="hero-title">Welcome to Tessavale Communications</h1>
    <div class="hero-actions">
      <span class="btn btn-primary">OUR SERVICES</span>
      <span class="btn btn-outline">TEAM</span>
    </div>
    <span class="slider-arrow prev">
      <svg width="10" height="18" viewBox="0 0 10 18" fill="none" stroke="#fff" stroke-width="1.4"><polyline points="9,1 1,9 9,17"/></svg>
    </span>
    <span class="slider-arrow next">
      <svg width="10" height="18" viewBox="0 0 10 18" fill="none" stroke="#fff" stroke-width="1.4"><polyline points="1,1 9,9 1,17"/></svg>
    </span>
    <div class="slider-dots"><span class="is-active"></span><span></span><span></span></div>
  </section>

  <section class="intro">
    <h2 class="intro-heading">Strategic Communications You Can Count On</h2>
    <div class="intro-rule"></div>
    <div class="intro-columns">
      <p>With more than 25 years of experience advising management teams in critical situations, we help our clients use their communications assets to protect, enhance, develop and defend their enterprise value — no matter what they are going through or where they are in the world. With approximately 700 expert strategic communications consultants in more than 25 key markets around the world, we combine global reach with critical local knowledge.</p>
      <p>We also have built an unrivaled depth of industry and interdisciplinary expertise so that clients have access to professionals who are focused on their particular sector; have a broad network of relationships with key influencers; and provide communications counsel based on in-depth industry knowledge and experience.</p>
    </div>
  </section>

  <section class="testimonial">
    <p class="testimonial-quote">"Thank you for all your work on our brand! It turned out perfect! "</p>
    <p class="testimonial-author">– Marc Delaney</p>
    <div class="testimonial-dots"><span class="is-active"></span><span></span></div>
  </section>

  <footer class="site-footer">
    <p class="copyright">© 2014 Tessavale Communications. Tessavale Communications</p>
    <div class="social"><span></span><span></span></div>
  </footer>
</body>
</html>
```